Bluewater Motor Finance Home Page

We need a desktop version mock up (we will base our mobile version off of this) of a website homepage for our auto loan business, Bluewater Motor Finance. This does not need to be a functioning site, just a home page mock up. We are based in the metro St. Louis, MO area. We offer "guaranteed" auto loans for all credit types. We specialize in financing for bad/no credit customers. We are able to help rebuild these type of customers' credit, all while putting them in a great late model vehicle they'll love. Our online credit app takes less than 60 seconds, doesn't require a SS# and gives a free credit score if they fill it out within 3 minutes. We are looking for an outside perspective to help us in this design process. We are not completely sure what we want, but we do want it to be professional and secure looking, all while being unique and aesthetically pleasing. We want the customer to be able to put in their zip code to be directed to the right location that can get them pre approved. I attached a wireframe with some stuff we'd like to include, but in no way does it have to be in the same layout or the same ideas. We want everyone to "go crazy" with their creative side on this. Our current site is awful, here is a link to get a better idea: www.bluewatermotorfinance-example.com. Attached is our logo too, base colors off of it. Watch our video that is also attached for a better idea.

Target Market(s)

Residents of the St. Louis Missouri Metro Area that need an auto loan. 24-55 Male and Female - Lots of "urban market" customers.

Industry/Entity Type

Loan

Number of Pages Required

1 page

Colors
9bcb3b

Requirements
Must have
• An area where the customer can enter their zip code - Be creative!
Nice to have
• See wireframe attachment for ideas - Be creative!

```html
<!DOCTYPE html>
<html lang="en">
<head>
<meta charset="utf-8">
<title>Bluewater Motor Finance</title>
<link href="https://fonts.googleapis.com/css2?family=Raleway:wght@400;500;600&family=Open+Sans:ital,wght@0,400;0,600;1,400&display=swap" rel="stylesheet">
<style>
:root{
  --green:#9bcb3b;
  --green-light:#b3dc5e;
  --green-dark:#6fab26;
  --yellow:#f7e81a;
  --ink:#222222;
  --body:#444444;
  --muted:#777777;
  --white:#ffffff;
  --grey-band:#f0f0f0;
  --footer:#1b1b1b;
}
*{margin:0;padding:0;box-sizing:border-box}
html,body{width:1200px;height:2557px;overflow:hidden}
body{position:relative;font-family:"Open Sans",Arial,sans-serif;color:var(--body);background:var(--white)}
.abs{position:absolute}
section,header,footer{position:absolute;left:0;width:1200px;overflow:hidden}

/* Hero */
.hero{top:0;height:580px}
.hero-photo{position:absolute;inset:0;background:linear-gradient(120deg,#5a4a3e 0%,#8a7360 30%,#a48c74 55%,#6e5a48 80%,#4a3d33 100%)}
.hero-shade{position:absolute;inset:0;background:linear-gradient(180deg,rgba(0,0,0,.35) 0,rgba(0,0,0,.1) 20%,rgba(0,0,0,.15) 100%)}
.brand{left:184px;top:36px;display:flex;align-items:center;gap:8px;font-family:"Raleway",sans-serif;font-weight:600;font-size:15px;color:var(--green);white-space:nowrap}
.brand-mark{width:22px;height:22px;background:var(--green)}
.nav{left:438px;top:40px;display:flex;gap:30px;font-family:"Raleway",sans-serif;font-size:16px;color:var(--white)}
.phone{left:885px;top:38px;display:flex;align-items:center;gap:6px;font-family:"Raleway",sans-serif;font-size:16px;color:var(--white)}
.hero-title{left:0;width:1200px;top:198px;text-align:center;font-family:"Raleway",sans-serif;font-size:41px;font-weight:400;color:var(--white)}
.hero-sub{left:0;width:1200px;top:256px;text-align:center;font-family:"Raleway",sans-serif;font-size:26px;color:var(--white)}
.zip-frame{left:285px;top:324px;width:383px;height:82px;background:var(--yellow);padding:8px}
.zip-inner{width:100%;height:100%;border:2px solid #222;display:flex;align-items:center;padding:0 13px}
.zip-input{flex:1;height:32px;background:var(--white);font-size:11px;color:var(--muted);padding:9px 14px}
.zip-btn{height:32px;background:#222;color:var(--white);font-size:12px;padding:8px 16px}
.perks{left:687px;top:322px;list-style:none;font-size:12.5px;color:var(--white)}
.perks li{display:flex;align-items:center;gap:8px;height:29px}
.arrow{top:302px}

/* Apply */
.apply{top:580px;height:85px;background:linear-gradient(180deg,#fafafa,#e9e9e9);display:flex;justify-content:center;align-items:center;gap:18px;font-family:"Raleway",sans-serif;font-size:16px}
.apply .label{font-size:20px;color:#333}
.timer{width:110px;height:34px;border:1px solid #bbb;background:var(--white);font-size:15px;color:var(--muted);padding:7px 16px}

/* Testimonials */
.testimonials{top:665px;height:310px;background:linear-gradient(180deg,var(--green-light),var(--green-dark));text-align:center;color:var(--white)}
.t-title{top:36px;left:0;width:1200px;font-family:"Raleway",sans-serif;font-size:28px;font-weight:400}
.avatar{left:545px;top:79px;width:74px;height:74px;border-radius:50%;border:3px solid var(--white);background:linear-gradient(135deg,#c9b39a,#6f5b48)}
.quote{left:270px;top:160px;width:630px;font-style:italic;font-size:11.5px;line-height:20px}
.qmark{position:absolute;font-family:Georgia,serif;font-size:40px;line-height:1;color:var(--white)}
.author{left:0;width:1200px;top:232px;font-weight:600;font-size:13px}
.city{left:0;width:1200px;top:252px;font-size:11px;opacity:.9}

/* Calculator band */
.calc{top:975px;height:271px}
.calc-photo{position:absolute;inset:0;background:linear-gradient(90deg,#3d4145 0%,#5c6064 35%,#6d6a66 60%,#3a3430 100%)}
.calc-shade{position:absolute;inset:0;background:rgba(0,0,0,.25)}
.calc-title{left:205px;top:92px;font-family:"Raleway",sans-serif;font-size:30px;font-weight:400;color:var(--white)}
.calc-sub{left:205px;top:135px;font-family:"Raleway",sans-serif;font-size:20px;color:var(--white)}
.calc-btn{left:806px;top:105px;width:168px;height:40px;border:2px solid var(--white);color:var(--white);font-family:"Raleway",sans-serif;font-size:15px;font-weight:500;text-align:center;line-height:36px}

/* Steps */
.step{height:260px}
.step1{top:1246px;background:var(--white)}
.step2{top:1506px;height:298px;background:var(--grey-band)}
.step3{top:1804px;height:269px;background:var(--white)}
.step h2{position:absolute;font-family:"Raleway",sans-serif;font-weight:400;font-size:29px;color:var(--ink)}
.step p{position:absolute;font-size:10px;line-height:17px;color:var(--body)}
.art{position:absolute}

/* Company band */
.company{top:2073px;height:345px}
.company-photo{position:absolute;inset:0;background:linear-gradient(90deg,#4d4a2c 0%,#8a7a45 20%,#6b6f4a 45%,#6c737a 70%,#4e5a4e 100%)}
.company-shade{position:absolute;inset:0;background:rgba(0,0,0,.25)}
.company h2{position:absolute;left:187px;top:86px;font-family:"Raleway",sans-serif;font-weight:400;font-size:30px;color:var(--white)}
.company p{position:absolute;left:187px;width:410px;font-size:10px;line-height:17px;color:var(--white)}
.video{left:650px;top:55px;width:368px;height:218px;border:6px solid var(--white);background:#2b2b2b}
.video-still{position:absolute;left:0;top:0;width:356px;height:176px;background:linear-gradient(120deg,#d9cfc8,#8e7a70 55%,#5a4a48)}
.video-bar{position:absolute;left:0;top:176px;width:356px;height:30px;background:#222}

/* Footer */
.footer{top:2418px;height:139px;background:var(--footer);color:var(--white)}
.f-links{left:428px;top:36px;display:flex;gap:36px;font-family:"Raleway",sans-serif;font-size:13px}
.f-copy{left:0;width:1200px;top:66px;text-align:center;font-size:11px;color:#bbb}
.social{left:887px;top:34px;display:flex;gap:6px}
.social span{width:28px;height:28px;border:1.5px solid var(--white);border-radius:50%}
</style>
</head>
<body>

<header class="hero">
  <div class="hero-photo" role="img" aria-label="Young couple smiling in a convertible car"></div>
  <div class="hero-shade"></div>
  <div class="abs brand"><span class="brand-mark"></span>Bluewater Motor Finance</div>
  <nav class="abs nav"><span>Locations</span><span>Finance Center</span><span>About</span><span>FAQ</span><span>Contact</span></nav>
  <div class="abs phone">
    <svg width="22" height="22" viewBox="0 0 22 22"><circle cx="11" cy="11" r="11" fill="#9bcb3b"/><path d="M7 6c1-1 2 0 2.5 1.5s-1 1.5-.5 2.5 2 2.5 3 3 1-1 2.5-.5 2.5 1.5 1.5 2.5-3 1-6-2-4-6-3-7z" fill="#fff"/></svg>
    (800) 555-0142
  </div>
  <svg class="abs arrow" style="left:50px" width="24" height="40" viewBox="0 0 24 40"><path d="M18 6 6 20l12 14" fill="none" stroke="#fff" stroke-width="4"/></svg>
  <svg class="abs arrow" style="left:1106px" width="24" height="40" viewBox="0 0 24 40"><path d="M6 6l12 14L6 34" fill="none" stroke="#fff" stroke-width="4"/></svg>
  <h1 class="abs hero-title">Over 30,000 Auto Loans Since 2000</h1>
  <p class="abs hero-sub">Pre-Approval in Under 60 Seconds!</p>
  <div class="abs zip-frame"><div class="zip-inner"><div class="zip-input">Enter Zip Code</div><div class="zip-btn">Get Approved</div></div></div>
  <ul class="abs perks">
    <li><svg width="14" height="12" viewBox="0 0 14 12"><path d="M1 6l4 4 8-9" fill="none" stroke="#fff" stroke-width="2.4"/></svg>No Social Security Number Required</li>
    <li><svg width="14" height="12" viewBox="0 0 14 12"><path d="M1 6l4 4 8-9" fill="none" stroke="#fff" stroke-width="2.4"/></svg>Instant Approval</li>
    <li><svg width="14" height="12" viewBox="0 0 14 12"><path d="M1 6l4 4 8-9" fill="none" stroke="#fff" stroke-width="2.4"/></svg>No Application Fees</li>
    <li><svg width="14" height="12" viewBox="0 0 14 12"><path d="M1 6l4 4 8-9" fill="none" stroke="#fff" stroke-width="2.4"/></svg>All Credit Accepted</li>
  </ul>
</header>

<section class="apply">
  <span class="label">Apply within</span>
  <span class="timer">3:00</span>
  <span>and see your credit score for free!</span>
</section>

<section class="testimonials">
  <h2 class="abs t-title">Testimonials</h2>
  <div class="abs avatar" role="img" aria-label="Customer portrait"></div>
  <span class="qmark" style="left:270px;top:144px">“</span>
  <p class="abs quote">Curabitur iaculis tempus eros Curabitur vel mi sit amet magna malesuada ultrices Ut nisi erat fermentum vel congue id euismod in elit Fusce ultricies orci commodo a mi Morbi ornare gravida elit Integer congue augue et malesuada iaculis ipsum dui aliquet felis</p>
  <span class="qmark" style="left:782px;top:202px">”</span>
  <p class="abs author">By Author Name</p>
  <p class="abs city">City Location</p>
</section>

<section class="calc">
  <div class="calc-photo" role="img" aria-label="Man working on a laptop outside an office building"></div>
  <div class="calc-shade"></div>
  <h2 class="abs calc-title">Sed metus augue convallis et vehicula</h2>
  <p class="abs calc-sub">Curabitur sit amet magna malesuada ultrices</p>
  <div class="abs calc-btn">Calculate Payment</div>
</section>

<section class="step step1">
  <h2 style="left:182px;top:60px">Step 1</h2>
  <p style="left:182px;top:102px;width:450px">Lorem ipsum dolor sit amet, consectetur adipiscing elit. Proin a elit vitae erat accumsan venenatis in efficitur velit. dapibus fringilla. Nulla varius eleifend risus non scelerisque. Morbi sapien lorem, gravida in ex in, finibus scelerisque massa. Quisque in vulputate magna</p>
  <p style="left:182px;top:166px;width:450px">Lorem ipsum dolor sit amet, consectetur adipiscing elit. Proin elit vitae erat accumsan venenatis in efficitur velit. dapibus fringilla. Nulla varius eleifend</p>
  <div class="art" style="left:699px;top:24px;width:290px;height:213px;background:linear-gradient(135deg,#cfd6dc,#9ccc5a 60%,#6aa83a)" role="img" aria-label="Isometric illustration of a city block with a location pin"></div>
</section>

<section class="step step2">
  <div class="art" style="left:222px;top:29px;width:213px;height:238px;background:linear-gradient(160deg,#e86a5a,#f2d36b 50%,#e3e0d4)" role="img" aria-label="Illustration of house, documents, calculator and savings"></div>
  <h2 style="left:549px;top:86px">Step 2</h2>
  <p style="left:549px;top:128px;width:480px">Lorem ipsum dolor sit amet, consectetur adipiscing elit. Proin a elit vitae erat accumsan venenatis in efficitur velit. dapibus fringilla. Nulla varius eleifend risus non scelerisque. Morbi sapien lorem, gravida in ex in, finibus scelerisque massa. Quisque in vulputate magna</p>
  <p style="left:549px;top:192px;width:480px">Lorem ipsum dolor sit amet, consectetur adipiscing elit. Proin elit vitae erat accumsan venenatis in efficitur velit. dapibus fringilla. Nulla varius eleifend</p>
</section>

<section class="step step3">
  <h2 style="left:182px;top:54px">Step 3</h2>
  <p style="left:182px;top:96px;width:440px">Lorem ipsum dolor sit amet, consectetur adipiscing elit. Proin a elit vitae erat accumsan venenatis in efficitur velit. dapibus fringilla. Nulla varius eleifend risus non scelerisque. Morbi sapien lorem, gravida in ex in, finibus scelerisque m</p>
  <p style="left:182px;top:160px;width:440px">Lorem ipsum dolor sit amet, consectetur adipiscing elit. Proin elit vitae erat accumsan venenatis in efficitur velit. dapibus fringilla. Nulla varius eleifend</p>
  <div class="art" style="left:648px;top:37px;width:384px;height:232px;background:linear-gradient(180deg,#fff 0%,#e8453c 30%,#f3f3f3 45%,#f4c9a8 70%,#2c3a5a 100%)" role="img" aria-label="Illustration of a hand presenting a red car on a tray"></div>
</section>

<section class="company">
  <div class="company-photo" role="img" aria-label="Country road through fields at sunset"></div>
  <div class="company-shade"></div>
  <h2>Bluewater Motor Finance</h2>
  <p style="top:135px">Lorem ipsum dolor sit amet, consectetur adipiscing elit. Proin a elit vitae erat accumsan venenatis in efficitur velit. dapibus fringilla. Nulla varius eleifend risus non scelerisque. Morbi sapien lorem, gravida in ex</p>
  <p style="top:199px">Lorem ipsum dolor sit amet, consectetur adipiscing elit. Proin elit vitae erat accumsan venenatis in efficitur velit. dapibus fringilla. Nulla varius eleifend</p>
  <div class="abs video">
    <div class="video-still" role="img" aria-label="Video still of a couple reviewing paperwork at home"></div>
    <svg class="abs" style="left:154px;top:64px" width="48" height="48" viewBox="0 0 48 48"><circle cx="24" cy="24" r="24" fill="#fff"/><path d="M19 14l15 10-15 10z" fill="#222"/></svg>
    <div class="video-bar">
      <svg width="356" height="30" viewBox="0 0 356 30"><path d="M10 10l8 5-8 5z" fill="#fff"/><rect x="30" y="13" width="262" height="4" fill="#555"/><rect x="30" y="13" width="95" height="4" fill="#fff"/><path d="M318 12h4l5-4v14l-5-4h-4z" fill="#fff"/><path d="M331 11q3 4 0 8" stroke="#fff" fill="none" stroke-width="1.5"/></svg>
    </div>
  </div>
</section>

<footer class="footer">
  <nav class="abs f-links"><span>HOME</span><span>ABOUT</span><span>PRIVACY</span><span>CONTACT</span></nav>
  <p class="abs f-copy">© 2016 Bluewater Motor Finance. All Rights Reserved.</p>
  <div class="abs social"><span></span><span></span><span></span><span></span></div>
</footer>

</body>
</html>
```